Velmora Diagnostics Website

Project Description – Velmora Website Design
We need a clean, modern, and professional website for Velmora Diagnostics, a Ashgrove Hollis University of Dunmere spin-out focused on early cancer detection. Our first product, GlandSURE™, is a urine-based risk assessment test for pancreatic cancer, supported by strong clinical validation and partnerships with leading hospitals.

The site should:

Communicate trust, innovation, and clinical credibility.
Feature a clear value proposition on the home page with strong calls to action for investors, clinicians, and partners.
Showcase our technology, science, and clinical evidence in a way that is accessible but authoritative.
Highlight our university heritage, team, and collaborators.
Include sections for products/services, news/press, and contact forms.
Be fully responsive, WordPress compatible, SEO-friendly, and WCAG 2.1 AA accessible.

We want a minimalist, elegant design with subtle animations, strong visuals (e.g., science/biotech imagery), and a clear structure for future growth.
Deliverables should include editable design files (Figma/Sketch/Adobe XD) and a style guide.

```html
<!DOCTYPE html>
<html lang="en">
<head>
<meta charset="utf-8">
<title>Velmora DX – Early Cancer Detection</title>
<link href="https://fonts.googleapis.com/css2?family=Figtree:wght@400;500;600;700&display=swap" rel="stylesheet">
<style>
:root{
  --blue:#3b89d6;
  --blue-dark:#2f78c4;
  --sky:#66c2ee;
  --yellow:#f5c535;
  --ink:#1e2330;
  --muted:#5b6270;
  --light:#f6f7f9;
  --white:#ffffff;
  --line:#d9dde3;
}
*{box-sizing:border-box;margin:0;padding:0}
html,body{width:1200px;height:2883px;overflow:hidden}
body{font-family:"Figtree",Arial,sans-serif;color:var(--ink);background:var(--white);position:relative}
.abs{position:absolute}
.btn{position:absolute;display:flex;align-items:center;justify-content:center;font-size:10px;font-weight:600;color:var(--white);height:31px;border-radius:2px}
.btn--primary{background:var(--blue)}
.btn--light{background:var(--sky)}

/* header */
.site-header{left:0;top:0;width:1200px;height:63px;background:var(--white);box-shadow:0 1px 4px rgba(0,0,0,.05);z-index:3}
.brand{position:absolute;display:flex;align-items:center;gap:8px;color:var(--blue);font-weight:600;letter-spacing:1.5px}
.brand__dot{border-radius:50%;background:var(--yellow)}
.site-header .brand{left:106px;top:13px;font-size:17px}
.site-header .brand__dot{width:24px;height:24px}
.nav{position:absolute;left:378px;top:0;display:flex;gap:25px;height:63px;align-items:center;font-size:9.5px;font-weight:500}
.nav a{color:var(--ink);text-decoration:none;position:relative;height:63px;display:flex;align-items:center}
.nav a.is-active{color:var(--blue)}
.nav a.is-active::after{content:"";position:absolute;left:-6px;right:-6px;bottom:0;height:2px;background:var(--blue)}
.search-icon{position:absolute;left:940px;top:19px;width:24px;height:24px;border:1px solid var(--sky);border-radius:50%}
.site-header .btn{left:984px;top:16px;width:110px}

/* hero */
.hero{left:0;top:63px;width:1200px;height:549px;background:linear-gradient(110deg,#fafbfc 0%,#fff 45%)}
.hero__accent{left:818px;top:0;width:382px;height:549px;background:var(--yellow)}
.hero__photo{left:525px;top:56px;width:675px;height:437px;background:linear-gradient(120deg,#eef1f4 0%,#dfe6ee 40%,#f2d8df 60%,#7fa85a 100%)}
.hero__title{left:106px;top:155px;font-size:31px;line-height:34px;font-weight:600;color:var(--blue)}
.hero__lead{left:106px;top:276px;font-size:24px;line-height:30px;font-weight:400}
.hero .btn--primary{left:106px;top:363px;width:109px}
.hero .btn--light{left:228px;top:363px;width:105px}

/* features */
.features{left:0;top:612px;width:1200px;height:530px;background:var(--blue)}
.features__title{left:0;top:76px;width:1200px;text-align:center;font-size:30px;line-height:35px;font-weight:600;color:var(--white)}
.card{position:absolute;top:210px;width:228px;height:182px;background:var(--white);padding:18px 18px}
.card__icon{width:44px;height:44px;border-radius:50%;border:2px solid var(--blue);background:#fdf3d2}
.card__title{margin-top:12px;font-size:12px;line-height:14px;font-weight:600;color:var(--blue)}
.card__text{margin-top:17px;font-size:8.5px;line-height:15px;color:var(--muted)}
.features .btn{left:557px;top:424px;width:85px}

/* video */
.video{left:0;top:1142px;width:1200px;height:500px;background:linear-gradient(100deg,#4d6a86 0%,#8fa7bd 35%,#c4cfd8 60%,#e6e9ec 80%,#9aa8b5 100%)}
.play{left:568px;top:218px;width:63px;height:63px;border-radius:50%;background:var(--yellow);display:flex;align-items:center;justify-content:center}

/* trust */
.trust__title{left:0;top:1717px;width:1200px;text-align:center;font-size:31px;font-weight:600;color:var(--blue)}
.stat{position:absolute;top:1782px;width:212px;height:212px;border-radius:50%;display:flex;flex-direction:column;align-items:center;justify-content:center}
.stat__label{font-size:9.5px;font-weight:600}
.stat__value{font-size:42px;font-weight:400;margin-top:4px}
.stat--a{left:298px;border:1px solid #6e9fd2;background:linear-gradient(180deg,#fff 0%,#dde6f0 100%)}
.stat--a .stat__value{color:var(--blue)}
.stat--b{left:494px;border:1px solid #ecd58a;background:linear-gradient(180deg,#fff 0%,#dff0f7 100%)}
.stat--b .stat__value{color:var(--yellow)}
.stat--c{left:690px;border:1px solid #9fd4ea;background:linear-gradient(180deg,#fff 0%,#fbf0d6 100%)}
.stat--c .stat__value{color:var(--sky)}
.trust-btns .btn--primary{left:499px;top:2027px;width:84px}
.trust-btns .btn--light{left:596px;top:2027px;width:105px}

/* demo */
.demo{left:0;top:2133px;width:1200px;height:430px;background:var(--blue)}
.demo__accent{left:1092px;top:0;width:108px;height:430px;background:var(--yellow)}
.demo__title{left:106px;top:146px;font-size:30px;line-height:35px;font-weight:600;color:var(--white)}
.demo__arrow{left:268px;top:190px}
.demo__lead{left:106px;top:244px;font-size:24px;line-height:30px;font-weight:400;color:#e8f1fb}
.field{position:absolute;background:var(--white);border-radius:2px;height:30px;font-size:9px;padding:0 12px;display:flex;align-items:center;color:var(--ink)}
.field--area{height:62px;align-items:flex-start;padding-top:11px}
.demo .btn{left:612px;top:303px;width:88px}

/* footer */
.site-footer{left:0;top:2563px;width:1200px;height:320px;background:var(--light)}
.site-footer .brand{left:106px;top:62px;font-size:23px}
.site-footer .brand__dot{width:58px;height:58px;background:radial-gradient(circle,var(--yellow) 30%,transparent 32%),radial-gradient(circle,#9fd1f0 60%,transparent 62%)}
.footer__about{left:106px;top:147px;width:330px;font-size:13px;line-height:19px}
.footer__divider{left:509px;top:0;width:1px;height:253px;background:var(--line)}
.to-top{left:497px;top:83px;width:24px;height:88px;border-radius:12px;background:var(--blue);color:var(--white);font-size:8px;font-weight:600;writing-mode:vertical-rl;transform:rotate(180deg);display:flex;align-items:center;justify-content:center}
.footer__col{position:absolute;top:68px;font-size:13px}
.footer__col h3{font-size:16px;font-weight:600;margin-bottom:18px}
.footer__col li{list-style:none;line-height:25px}
.footer__col--links{left:587px}
.footer__col--legal{left:738px}
.footer__col--support{left:904px}
.footer__col--support p{font-size:15px;line-height:29px}
.footer__col--support span{color:var(--blue)}
.socials{display:flex;gap:8px;margin-top:8px}
.socials i{width:24px;height:24px;border:1px solid var(--blue);border-radius:50%;display:flex;align-items:center;justify-content:center}
.footer__rule{left:106px;top:254px;width:988px;height:1px;background:var(--line)}
.footer__legal{left:106px;top:282px;font-size:9.5px;font-weight:500}
.footer__legal span{color:var(--blue)}
.badge{position:absolute;top:272px;height:34px}
.badge--a{left:904px;width:42px;border-radius:50%;background:#2c8fa8}
.badge--b{left:966px;width:90px;border-radius:4px;background:#d8dbe4}
</style>
</head>
<body>

<header class="abs site-header">
  <div class="brand"><span class="brand__dot"></span>Velmora DX</div>
  <nav class="nav">
    <a class="is-active" href="#">Home</a>
    <a href="#">About us</a>
    <a href="#">Services</a>
    <a href="#">Technology</a>
    <a href="#">Science</a>
    <a href="#">Partners &amp; Collaborations</a>
    <a href="#">News</a>
    <a href="#">Contact us</a>
  </nav>
  <span class="search-icon" aria-hidden="true"></span>
  <a class="btn btn--primary">Request a Demo</a>
</header>

<section class="abs hero">
  <div class="abs hero__accent"></div>
  <div class="abs hero__photo" role="img" aria-label="Clinician in white coat holding a pink awareness ribbon"></div>
  <h1 class="abs hero__title">Lighting the<br>Way to Early Cancer<br>Detection</h1>
  <p class="abs hero__lead">highlight non-invasive,<br>urine-based diagnostics.</p>
  <a class="btn btn--primary">Request a Demo</a>
  <a class="btn btn--light">Partner with Us</a>
</section>

<section class="abs features">
  <h2 class="abs features__title">Combining biomarker panels with advanced<br>analytics for surveillance and early<br>detection of cancer</h2>
  <article class="card" style="left:106px">
    <div class="card__icon" role="img" aria-label="Non-invasive icon"></div>
    <h3 class="card__title">Non-Invasive,<br>Painless</h3>
    <p class="card__text">It is a long established fact that a reader will be distracted by the readable content of a page when looking.</p>
  </article>
  <article class="card" style="left:359px">
    <div class="card__icon" role="img" aria-label="Biomarker icon"></div>
    <h3 class="card__title">Precision<br>Biomarkers</h3>
    <p class="card__text">It is a long established fact that a reader will be distracted by the readable content of a page when looking.</p>
  </article>
  <article class="card" style="left:612px">
    <div class="card__icon" role="img" aria-label="AI insights icon"></div>
    <h3 class="card__title">AI-Powered<br>Insights</h3>
    <p class="card__text">It is a long established fact that a reader will be distracted by the readable content of a page when looking.</p>
  </article>
  <article class="card" style="left:865px">
    <div class="card__icon" role="img" aria-label="Clinical validation icon"></div>
    <h3 class="card__title">Clinically Validated &amp;<br>University Spin-Out Heritage</h3>
    <p class="card__text">It is a long established fact that a reader will be distracted by the readable content of a page when looking.</p>
  </article>
  <a class="btn btn--light">Learn More</a>
</section>

<section class="abs video" role="img" aria-label="Doctor using a tablet beside a DNA helix and medical data overlay">
  <div class="abs play">
    <svg width="18" height="20" viewBox="0 0 18 20" aria-hidden="true"><path d="M2 1 L17 10 L2 19 Z" fill="#fff"/></svg>
  </div>
</section>

<h2 class="abs trust__title">Why Trust on Velmora DX</h2>
<div class="stat stat--a"><span class="stat__label">Sensitivity</span><span class="stat__value">86%</span></div>
<div class="stat stat--b"><span class="stat__label">Specificity</span><span class="stat__value">90%</span></div>
<div class="stat stat--c"><span class="stat__label">Samples Validated</span><span class="stat__value">1,000</span></div>
<div class="trust-btns">
  <a class="btn btn--primary">Contact Us</a>
  <a class="btn btn--light">Partner with Us</a>
</div>

<section class="abs demo">
  <div class="abs demo__accent"></div>
  <h2 class="abs demo__title">Request a demo for<br>clinicians</h2>
  <svg class="abs demo__arrow" width="222" height="10" viewBox="0 0 222 10" aria-hidden="true"><path d="M0 5 H220 M215 1 L220 5 L215 9" stroke="#fff" fill="none" stroke-width="1"/></svg>
  <p class="abs demo__lead">Today is the perfect day to<br>get started.</p>
  <form>
    <div class="field" style="left:612px;top:97px;width:188px">Name</div>
    <div class="field" style="left:812px;top:97px;width:188px">Phone</div>
    <div class="field" style="left:612px;top:141px;width:388px">Enter Your Email...</div>
    <div class="field" style="left:612px;top:185px;width:388px;justify-content:space-between">Select Service
      <svg width="10" height="6" viewBox="0 0 10 6" aria-hidden="true"><path d="M1 1 L5 5 L9 1" stroke="#1e2330" fill="none" stroke-width="1.4"/></svg></div>
    <div class="field field--area" style="left:612px;top:228px;width:388px">Type your message...</div>
    <a class="btn btn--light">Get a Demo</a>
  </form>
</section>

<footer class="abs site-footer">
  <div class="brand"><span class="brand__dot"></span>Velmora DX</div>
  <p class="abs footer__about">Lorem Ipsum is simply dummy text of the printing and typesetting industry lorem ipsum has been the industry's standard dummy.</p>
  <div class="abs footer__divider"></div>
  <div class="abs to-top">Back to top ↑</div>
  <div class="footer__col footer__col--links"><h3>Quick links</h3><ul><li>Home</li><li>About</li><li>Science</li><li>Contact</li></ul></div>
  <div class="footer__col footer__col--legal"><h3>Legal</h3><ul><li>Privacy Policy</li><li>Terms of Use</li><li>GDPR</li><li>Accessibility</li></ul></div>
  <div class="footer__col footer__col--support"><h3>Get Support</h3>
    <p><span>P.</span> (201)555-0148</p>
    <p><span>E.</span> info@velmoradx.com</p>
    <div class="socials">
      <i aria-hidden="true"><svg width="8" height="8"><circle cx="4" cy="4" r="3" fill="#3b89d6"/></svg></i>
      <i aria-hidden="true"><svg width="8" height="10" viewBox="0 0 8 10"><path d="M4 9 C1 5 1 4 1 3.5 A3 3 0 0 1 7 3.5 C7 4 7 5 4 9Z" fill="#3b89d6"/></svg></i>
    </div>
  </div>
  <div class="abs footer__rule"></div>
  <p class="abs footer__legal">© 2025 <span>Velmora DX.</span> All rights reserved. &nbsp;&nbsp;&nbsp; I &nbsp;&nbsp;&nbsp; Registry ID: VDX00482913</p>
  <div class="badge badge--a" role="img" aria-label="Patent badge"></div>
  <div class="badge badge--b" role="img" aria-label="Partner badge"></div>
</footer>

</body>
</html>
```